Business Cards Brookvale
Biz_cards_Brookvale
Professional
Dwight Omsen, MD, PhD
418 Pennock Hollow Rd
Jackson, TN 38305
domsen@brookvalespine.com
www.brookvalespine.com
Here is logo specs:
Brookvale Spine Institute
Fonts:
Trajan Pro (Regular)
" " " " (Bold)
Colors:
Dark Blue : R: 3 G: 34 B: 87
Light Blue : R: 0 G: 102 B: 187
Dark Red : R: 130 G: 0 B: 0
Light Green : R: 255 G: 0 B: 0

```html
<!DOCTYPE html>
<html lang="en">
<head>
<meta charset="utf-8">
<title>Brookvale Spine Institute – Business Cards</title>
<link href="https://fonts.googleapis.com/css2?family=Cinzel:wght@400;700&display=swap" rel="stylesheet">
<style>
  :root {
    --dark-blue: rgb(3, 34, 87);
    --light-blue: rgb(0, 102, 187);
    --dark-red: rgb(130, 0, 0);
    --ink: #2a3550;
    --paper: #ffffff;
    --backdrop: #b9bcc0;
  }
  * { margin: 0; padding: 0; box-sizing: border-box; }
  html, body {
    width: 1200px; height: 895px; overflow: hidden;
    background: var(--backdrop);
    font-family: "Cinzel", serif;
  }
  .stage {
    width: 1200px; height: 895px;
    display: flex; flex-direction: column;
    align-items: center; justify-content: center; gap: 40px;
  }
  .card {
    width: 700px; height: 400px;
    position: relative;
    box-shadow: 0 6px 18px rgba(0,0,0,.18);
  }
  /* Front */
  .card-front { background: var(--paper); color: var(--ink); }
  .brand {
    position: absolute; left: 56px; top: 58px;
    display: flex; align-items: center; gap: 14px;
  }
  .brand-dot {
    width: 30px; height: 30px; border-radius: 50%;
    background: var(--dark-blue);
  }
  .brand-name {
    font-weight: 700; font-size: 30px; letter-spacing: 1px;
    color: var(--dark-red); line-height: 1.05;
  }
  .holder {
    position: absolute; left: 0; right: 0; top: 196px;
    text-align: center;
    font-size: 19px; font-weight: 400; letter-spacing: 1.5px;
    color: var(--dark-blue);
  }
  .contacts {
    position: absolute; left: 48px; right: 48px; bottom: 50px;
    display: flex; flex-direction: column; gap: 12px;
    font-size: 12px; letter-spacing: .6px; color: var(--ink);
  }
  .contact-row { display: flex; justify-content: space-between; }
  .contact { display: flex; align-items: center; gap: 7px; }
  .contact svg { width: 16px; height: 16px; flex: none; }
  /* Back */
  .card-back {
    background: radial-gradient(ellipse at 50% 40%, var(--light-blue) 0%, var(--dark-blue) 85%);
    color: var(--paper);
    display: flex; flex-direction: column;
    align-items: center; justify-content: center; gap: 28px;
  }
  .back-brand {
    display: flex; align-items: center; gap: 14px;
  }
  .back-brand .brand-dot { background: var(--paper); width: 34px; height: 34px; }
  .back-brand .brand-name { color: var(--paper); font-size: 34px; }
  .back-web { font-size: 15px; letter-spacing: 4px; }
</style>
</head>
<body>
<main class="stage">
  <section class="card card-front" aria-label="Business card front">
    <div class="brand">
      <span class="brand-dot"></span>
      <span class="brand-name">Brookvale Spine Institute</span>
    </div>
    <p class="holder">Dwight Omsen, MD, PhD</p>
    <div class="contacts">
      <div class="contact-row">
        <span class="contact">
          <svg viewBox="0 0 16 16" aria-hidden="true"><circle cx="8" cy="8" r="8" fill="var(--dark-blue)"/><path d="M8 3.5a3 3 0 0 0-3 3c0 2.2 3 5.5 3 5.5s3-3.3 3-5.5a3 3 0 0 0-3-3zm0 4.2a1.2 1.2 0 1 1 0-2.4 1.2 1.2 0 0 1 0 2.4z" fill="#fff"/></svg>
          418 Pennock Hollow Rd, Jackson, TN 38305
        </span>
        <span class="contact">
          <svg viewBox="0 0 16 16" aria-hidden="true"><circle cx="8" cy="8" r="8" fill="var(--dark-blue)"/><path d="M5.2 4h1.6l.8 2-1 .8a6 6 0 0 0 2.6 2.6l.8-1 2 .8v1.6c0 .5-.4.9-.9.9A7.3 7.3 0 0 1 4.3 4.9c0-.5.4-.9.9-.9z" fill="#fff"/></svg>
          731-555-0146
        </span>
        <span class="contact">
          <svg viewBox="0 0 16 16" aria-hidden="true"><circle cx="8" cy="8" r="8" fill="var(--dark-blue)"/><path d="M5.2 4h1.6l.8 2-1 .8a6 6 0 0 0 2.6 2.6l.8-1 2 .8v1.6c0 .5-.4.9-.9.9A7.3 7.3 0 0 1 4.3 4.9c0-.5.4-.9.9-.9z" fill="#fff"/></svg>
          731-555-0182
        </span>
      </div>
      <div class="contact-row">
        <span class="contact">
          <svg viewBox="0 0 16 16" aria-hidden="true"><circle cx="8" cy="8" r="8" fill="var(--dark-blue)"/><path d="M5.2 4h1.6l.8 2-1 .8a6 6 0 0 0 2.6 2.6l.8-1 2 .8v1.6c0 .5-.4.9-.9.9A7.3 7.3 0 0 1 4.3 4.9c0-.5.4-.9.9-.9z" fill="#fff"/></svg>
          1-877-555-0193
        </span>
        <span class="contact">
          <svg viewBox="0 0 16 16" aria-hidden="true"><circle cx="8" cy="8" r="8" fill="var(--dark-blue)"/><rect x="4" y="5" width="8" height="6" rx=".6" fill="#fff"/><path d="M4.3 5.4 8 8.3l3.7-2.9" stroke="var(--dark-blue)" stroke-width=".9" fill="none"/></svg>
          domsen@brookvalespine.com
        </span>
        <span class="contact">
          <svg viewBox="0 0 16 16" aria-hidden="true"><circle cx="8" cy="8" r="8" fill="var(--dark-blue)"/><circle cx="8" cy="8" r="4" stroke="#fff" stroke-width="1" fill="none"/><path d="M4 8h8M8 4c-1.6 2.4-1.6 5.6 0 8M8 4c1.6 2.4 1.6 5.6 0 8" stroke="#fff" stroke-width=".8" fill="none"/></svg>
          www.brookvalespine.com
        </span>
      </div>
    </div>
  </section>

  <section class="card card-back" aria-label="Business card back">
    <div class="back-brand">
      <span class="brand-dot"></span>
      <span class="brand-name">Brookvale</span>
    </div>
    <p class="back-web">www.brookvalespine.com</p>
  </section>
</main>
</body>
</html>
```